Northfield Builders Guild Business card

We are looking for a new business card design with photo included.
Our business is a nonprofit construction contractor membership organization. We offer business education, assist with business setup and licensing, provide safety training, and provide a member directory.
URL: www.brickwayguildnetwork.org
Color code:
CMYK: 0 cyan, 42 magenta, 100 yellow, 0 black for Print.
Hexidecimal: #FF9900
RGB: R 255; G 153; B 0

```html
<!DOCTYPE html>
<html lang="en">
<head>
<meta charset="utf-8">
<title>Northfield Builders Guild – Business Card</title>
<link href="https://fonts.googleapis.com/css2?family=Poppins:wght@400;500;700;800&display=swap" rel="stylesheet">
<style>
  :root {
    --orange: #ff9900;
    --charcoal: #2e2e30;
    --ink: #1f1f21;
    --paper: #ffffff;
    --backdrop: #d9d9db;
    --card-dark: #2b2b2d;
    --photo-top: #e9e6e3;
    --photo-bottom: #3a302c;
  }
  * { box-sizing: border-box; margin: 0; padding: 0; }
  html, body { width: 1200px; height: 900px; overflow: hidden; }
  body {
    background: var(--backdrop);
    font-family: "Poppins", sans-serif;
    color: var(--ink);
    position: relative;
  }
  .card {
    position: absolute;
    left: 300px;
    width: 600px;
    height: 343px;
    border-radius: 4px;
    box-shadow: 0 10px 28px rgba(0,0,0,.22);
    overflow: hidden;
  }
  .card--front { top: 60px; background: var(--paper); }
  .card--back { top: 470px; background: var(--card-dark); display: flex; align-items: center; justify-content: center; }

  .edge-band { position: absolute; top: 0; bottom: 0; }
  .edge-band--dark { left: 0; width: 12px; background: var(--charcoal); }
  .edge-band--orange { left: 18px; width: 9px; background: var(--orange); }

  .brand-name {
    position: absolute; left: 62px; top: 46px;
    font-weight: 800; font-size: 24px; line-height: 1.05;
    color: var(--ink); letter-spacing: .2px; width: 240px;
  }

  .identity { position: absolute; left: 62px; top: 126px; width: 310px; }
  .person-name { font-weight: 500; font-size: 18px; line-height: 24px; }
  .role-row { display: flex; align-items: center; gap: 10px; }
  .person-role { font-size: 13px; line-height: 18px; flex: none; }
  .divider { flex: 1; height: 2px; background: var(--orange); }

  .contact-list { position: absolute; left: 62px; top: 186px; list-style: none; }
  .contact-list li { display: flex; align-items: center; gap: 10px; font-size: 13px; line-height: 22px; }
  .contact-list svg { width: 14px; height: 14px; flex: none; }

  .address { position: absolute; left: 62px; top: 266px; font-size: 13.5px; line-height: 20px; font-style: normal; }

  .photo-area {
    position: absolute; right: 40px; top: 30px; bottom: 0; width: 190px;
    background: linear-gradient(180deg, var(--photo-top) 0%, var(--photo-bottom) 100%);
    border-radius: 90px 90px 0 0;
  }

  .back-brand { font-weight: 800; font-size: 34px; color: var(--orange); }
</style>
</head>
<body>
  <section class="card card--front">
    <div class="edge-band edge-band--dark"></div>
    <div class="edge-band edge-band--orange"></div>

    <div class="brand-name">Northfield Builders Guild</div>

    <div class="identity">
      <div class="person-name">Morgan Ellery</div>
      <div class="role-row">
        <div class="person-role">Director</div>
        <div class="divider"></div>
      </div>
    </div>

    <ul class="contact-list">
      <li>
        <svg viewBox="0 0 24 24" fill="none" stroke="#ff9900" stroke-width="2"><path d="M5 3h4l2 5-3 2a12 12 0 0 0 6 6l2-3 5 2v4a2 2 0 0 1-2 2A17 17 0 0 1 3 5a2 2 0 0 1 2-2z"/></svg>
        (503) 555-0187
      </li>
      <li>
        <svg viewBox="0 0 24 24" fill="none" stroke="#ff9900" stroke-width="2"><rect x="3" y="5" width="18" height="14" rx="1"/><path d="M3 6l9 7 9-7"/></svg>
        info@brickwayguildnetwork.org
      </li>
      <li>
        <svg viewBox="0 0 24 24" fill="none" stroke="#ff9900" stroke-width="2"><circle cx="12" cy="12" r="9"/><path d="M3 12h18M12 3c3 3 3 15 0 18M12 3c-3 3-3 15 0 18"/></svg>
        brickwayguildnetwork.org
      </li>
    </ul>

    <address class="address">
      2400 Harrow Creek Avenue<br>
      Millbrook, OR 97000
    </address>

    <div class="photo-area" role="img" aria-label="Portrait photo of the director in a dark business suit"></div>
  </section>

  <section class="card card--back">
    <div class="back-brand">Northfield Builders Guild</div>
  </section>
</body>
</html>
```